Cover of the e-book award-winning national sports figure.

I would like to utilize the picture this attached to this brief. If you could pull the trophies and myself out and place with the new background, that’s what I would like to see . I would like to have a new bookcover design for my e-book. I attached below the original cover and have marked in red. The things that I don’t want on the new cover. I’ve attached a picture that’s not the original. I’m waiting on the high copy. I would like to replace the old logo with the one that I have attached. The website that I would like to have on the book is www.dellanvmoreaux.com.
Target Market(s)
Biography
Industry/Entity Type
Sports & motivation?
Requirements
Must have
- Picture of me in the blue suit on the cover the title of the book walking past midnight lessons from quiet harbors
Nice to have
- Utilize the old cover that I have attached for some ideas
Should not have
- The cover should not have anything related to marlow crest press Inc.

```html
<!DOCTYPE html>
<html lang="en">
<head>
<meta charset="utf-8">
<title>Walking Past Midnight — Cover and Jacket</title>
<link rel="stylesheet" href="https://fonts.googleapis.com/css2?family=Oswald:wght@300;400;700&family=Montserrat:wght@400;600;700&display=swap">
<style>
:root{
  --navy-deep:#0a1740;
  --navy:#12306f;
  --navy-glow:#1f4ea6;
  --blue:#1f7fe0;
  --white:#ffffff;
  --ink:#1b1b1b;
  --stage:#9b9b9b;
  --stage-light:#d3d3d3;
  --title:'Oswald',sans-serif;
  --body:'Montserrat',sans-serif;
}
*{margin:0;padding:0;box-sizing:border-box}
html,body{width:1200px;height:2793px;overflow:hidden}
body{background:var(--stage);position:relative;font-family:var(--body);color:var(--ink)}
.stage-lower{position:absolute;left:0;top:2120px;width:1200px;height:673px;background:var(--stage-light)}

/* Front cover */
.cover{position:absolute;left:300px;top:200px;width:600px;height:800px;background:var(--white);overflow:hidden}
.cover .night{position:absolute;left:0;top:0;width:100%;height:540px;
  background:radial-gradient(ellipse at 70% 55%,var(--navy-glow) 0%,var(--navy) 45%,var(--navy-deep) 100%)}
.portrait{position:absolute;background:linear-gradient(180deg,#6b4a3a 0%,#22408c 18%,#1b3478 60%,#152a60 100%)}
.trophies{position:absolute;background:linear-gradient(180deg,#d9dde3 0%,#9aa1ab 40%,#6b4a32 62%,#4a2f1e 100%)}
.cover .portrait{right:0;top:310px;width:230px;height:490px;border-radius:110px 110px 0 0}
.cover .trophies{left:232px;top:460px;width:140px;height:340px;border-radius:40px 40px 0 0}
.title{position:absolute;font-family:var(--title);text-transform:uppercase;line-height:.9;z-index:2}
.title .big{display:block;font-weight:700;color:var(--white)}
.title .link{display:block;font-weight:300;color:var(--blue)}
.title .strong{display:block;font-weight:700;color:var(--blue)}
.subtitle{position:absolute;font-family:var(--title);color:var(--white);text-transform:uppercase;line-height:1;z-index:2}
.subtitle .light{font-weight:300;display:block}
.subtitle .bold{font-weight:700;display:block}
.cover .title{left:50px;top:60px}
.cover .title .big{font-size:128px;letter-spacing:-1px}
.cover .title .link{font-size:56px;margin-top:8px}
.cover .title .strong{font-size:82px;margin-top:2px}
.cover .subtitle{left:60px;top:372px;font-size:38px}
.author{position:absolute;font-family:var(--title);color:var(--blue);line-height:1;text-transform:uppercase;z-index:2}
.author .first{display:block;font-weight:700}
.author .last{display:block;font-weight:300}
.cover .author{left:60px;top:572px;font-size:42px}
.rule{position:absolute;height:1px;background:#9aa0aa}
.cover .rule{left:60px;top:672px;width:135px}
.foreword{position:absolute;font-family:var(--body);font-size:15px;line-height:1.15;color:var(--ink)}
.foreword strong{display:block;font-weight:700;margin-top:8px}
.cover .foreword{left:62px;top:688px}

/* Jacket spread */
.jacket{position:absolute;left:67px;top:2216px;width:1067px;height:462px;background:var(--white);overflow:hidden}
.panel{position:absolute;top:0;height:462px}
.flap-left{left:0;width:193px;padding:24px 18px 0 22px}
.back{left:193px;width:315px}
.spine{left:508px;width:54px}
.front{left:562px;width:300px}
.flap-right{left:862px;width:205px;padding:24px 18px 0 16px}
.dark{position:absolute;left:0;top:0;width:100%;height:310px;background:linear-gradient(180deg,var(--navy-deep),var(--navy))}
.front .dark{background:radial-gradient(ellipse at 70% 60%,var(--navy-glow) 0%,var(--navy) 45%,var(--navy-deep) 100%)}
.fine{font-size:4.6px;line-height:1.45;color:#333;margin-bottom:5px;text-align:justify}
.fine b{font-weight:700}
.fine-head{font-size:5px;font-weight:700;color:var(--blue);margin:6px 0 2px}
.visit{font-size:5.5px;font-weight:700;color:var(--blue);margin-top:6px}
.mark{display:flex;align-items:center;gap:5px;font-family:var(--body);font-weight:700;color:var(--navy-deep);text-transform:uppercase;position:absolute}
.mark i{display:block;border-radius:50%;background:var(--blue)}
.flap-left .mark{left:40px;top:392px;font-size:8px}
.flap-left .mark i{width:20px;height:20px}

.back .title{left:60px;top:30px}
.back .title .big{font-size:52px}
.back .title .link{font-size:22px;margin-top:3px}
.back .title .strong{font-size:34px}
.back .subtitle{left:62px;top:142px;font-size:13px;white-space:nowrap}
.back .subtitle .light,.back .subtitle .bold{display:inline}
.action-photo{position:absolute;left:30px;top:194px;width:92px;height:86px;
  background:linear-gradient(160deg,#3d5a3a 0%,#7c8a86 45%,#2a3b5e 100%)}
.intro{position:absolute;left:132px;top:190px;width:160px}
.intro .fine-head{margin-top:0;font-size:5.5px}
.intro .fine{color:#e8ecf5}
.back .mark{left:40px;top:350px;font-size:9px}
.back .mark i{width:26px;height:26px}
.site{position:absolute;font-size:6px;font-weight:700;color:var(--blue)}
.back .site{left:44px;top:398px}
.charity{position:absolute;left:170px;top:330px;width:115px;font-size:6.5px;line-height:1.3;color:#222}
.charity b{font-weight:700}

.spine-text{position:absolute;left:14px;top:34px;writing-mode:vertical-rl;font-family:var(--title);font-size:17px;white-space:nowrap;text-transform:uppercase;color:var(--white)}
.spine-text .a{color:var(--blue);font-weight:700}
.spine-text .sep{font-weight:300;margin:8px 0;color:var(--white)}
.spine-text .t{font-weight:400}
.spine-sub{position:absolute;left:18px;top:318px;writing-mode:vertical-rl;font-family:var(--title);font-size:8px;font-weight:700;line-height:1.05;color:var(--blue);text-transform:uppercase}
.spine .mark{left:16px;top:420px}
.spine .mark i{width:20px;height:20px}

.front .portrait{right:0;top:175px;width:108px;height:287px;border-radius:54px 54px 0 0}
.front .trophies{left:110px;top:272px;width:76px;height:190px;border-radius:22px 22px 0 0}
.front .title{left:26px;top:34px}
.front .title .big{font-size:66px}
.front .title .link{font-size:29px;margin-top:3px}
.front .title .strong{font-size:40px;margin-top:1px}
.front .subtitle{left:28px;top:196px;font-size:19px}
.front .author{left:28px;top:320px;font-size:21px}
.front .rule{left:28px;top:370px;width:68px}
.front .foreword{left:28px;top:378px;font-size:7.5px}
.front .foreword strong{margin-top:4px}

.flap-right .title{position:relative;top:auto;left:auto;margin-bottom:5px}
.flap-right .title .big{font-size:44px;color:var(--navy-deep)}
.flap-right .title .link{font-size:12px;margin-top:2px}
.flap-right .title .strong{font-size:28px}
.flap-right .sub-inline{font-family:var(--title);font-size:11px;line-height:1;color:var(--navy-deep);text-transform:uppercase;white-space:nowrap;margin-bottom:10px}
.flap-right .sub-inline .light{font-weight:300}
.flap-right .sub-inline .bold{font-weight:700}
</style>
</head>
<body>
<div class="stage-lower"></div>

<section class="cover" aria-label="E-book front cover">
  <div class="night"></div>
  <div class="trophies" role="img" aria-label="Two silver championship trophies on a wooden side table"></div>
  <div class="portrait" role="img" aria-label="The author standing in a blue pinstripe suit"></div>
  <h1 class="title"><span class="big">Walking</span><span class="link">Past</span><span class="strong">Midnight</span></h1>
  <p class="subtitle"><span class="light">Lessons</span><span class="bold">From Quiet</span><span class="bold">Harbors</span></p>
  <p class="author"><span class="first">Dellan</span><span class="last">Moreaux</span></p>
  <div class="rule"></div>
  <p class="foreword">Foreword<br>by<strong>MARCUS HALE</strong></p>
</section>

<section class="jacket" aria-label="Print jacket spread">
  <div class="panel flap-left">
    <p class="fine">(Continued from front flap)</p>
    <p class="fine">which required that he prove himself as a walk-on, academically and athletically, during his first year. By his second season he had become a valued member of the special teams unit, earning the trust of coaches and teammates alike. Years of steady work followed, and he finally earned the starting role at fullback, leading the way for a record-setting ground game.</p>
    <p class="fine">In <b>WALKING PAST MIDNIGHT</b>, which is part memoir and part playbook, the author offers a framework for becoming an effective and generous team player, on the field and off it.</p>
    <p class="fine-head">DELLAN MOREAUX</p>
    <p class="fine">played fullback for nine professional seasons and won two championships. He speaks to schools, companies and community groups, and lives in Colorado with his family.</p>
    <p class="visit">Visit www.dellanvmoreaux.com for the author web page.</p>
    <div class="mark"><i></i>Dellan Moreaux</div>
  </div>

  <div class="panel back">
    <div class="dark"></div>
    <h2 class="title"><span class="big">Walking</span><span class="link">Past</span><span class="strong">Midnight</span></h2>
    <p class="subtitle"><span class="light">Lessons </span><span class="bold">From Quiet Harbors</span></p>
    <div class="action-photo" role="img" aria-label="Football action shot of a ball carrier breaking a tackle"></div>
    <div class="intro">
      <p class="fine-head">FROM DELLAN MOREAUX'S<br>INTRODUCTION</p>
      <p class="fine">Learning to trust the people beside you is essential to any lasting success. Within a shared effort, each person grows stronger than they could alone. I have felt the quiet pride of knowing I helped move a group of people one step closer to a common goal. The lessons in this book can serve any team, whether it is a company, a league or a family.</p>
    </div>
    <div class="mark"><i></i>Dellan Moreaux</div>
    <p class="site">www.dellanvmoreaux.com</p>
    <p class="charity">A portion of the proceeds from the <b>sale of this book will be donated to charity.</b></p>
  </div>

  <div class="panel spine">
    <div class="dark"></div>
    <p class="spine-text"><span class="a">Moreaux</span><span class="sep">|</span><span class="t">Walking Past Midnight</span></p>
    <p class="spine-sub">Lessons from<br>quiet harbors</p>
    <div class="mark"><i></i></div>
  </div>

  <div class="panel front">
    <div class="dark"></div>
    <div class="trophies" role="img" aria-label="Two silver championship trophies on a wooden side table"></div>
    <div class="portrait" role="img" aria-label="The author standing in a blue pinstripe suit"></div>
    <h2 class="title"><span class="big">Walking</span><span class="link">Past</span><span class="strong">Midnight</span></h2>
    <p class="subtitle"><span class="light">Lessons</span><span class="bold">From Quiet</span><span class="bold">Harbors</span></p>
    <p class="author"><span class="first">Dellan</span><span class="last">Moreaux</span></p>
    <div class="rule"></div>
    <p class="foreword">Foreword<br>by<strong>MARCUS HALE</strong></p>
  </div>

  <div class="panel flap-right">
    <h2 class="title"><span class="big">Walking</span><span class="link">Past</span><span class="strong">Midnight</span></h2>
    <p class="sub-inline"><span class="light">Lessons </span><span class="bold">From Quiet Harbors</span></p>
    <p class="fine">As the starting fullback for a championship club, the author cleared the path for a legendary running back and built a name as the ultimate team player. In this book he uses football as a lens for how to show up for others, how to push past limits, and how to turn personal setbacks into shared victories.</p>
    <p class="fine">Born and raised on the south side of a busy city, he chose early on that football would shape his life. He earned his place through effort rather than reputation, guided by coaches who believed in discipline, and he carried those habits into every locker room that followed.</p>
    <p class="fine">Though few recruiters noticed him at first, he turned down easier offers and chose the harder road toward the professional game.</p>
    <p class="fine">(Continued on back flap)</p>
  </div>
</section>
</body>
</html>
```